My project benefits Military, First Responders, Police, Fire, and Educators.

Contact Information for Business Card

2 Sided appointment card. Visual side will have my head shot with "Kestrel Works" in a bold graffic/text. I am picturing maybe the headshot applied to a filter that has a matrix effect where the picture is made up of data/numbers flowing vertically through the photo. I am of course open to other concepts as well. Side two will have contact info presented in an attractive visual complimenting the front.

```html
<!DOCTYPE html>
<html lang="en">
<head>
<meta charset="utf-8">
<title>Kestrel Works – Appointment Card</title>
<link rel="stylesheet" href="https://fonts.googleapis.com/css2?family=Oswald:wght@700&family=Open+Sans:wght@400;600;700&display=swap">
<style>
  :root {
    --backdrop: #3a322f;
    --card-dark: #1f1f20;
    --card-dark-edge: #2a2a2b;
    --ink: #1a1a1a;
    --paper: #f4f4f2;
    --white: #ffffff;
    --muted: #d8d8d8;
    --rule: #555555;
    --photo-top: #3c3a38;
    --photo-mid: #9c7a62;
    --photo-low: #1e2a44;
  }
  * { box-sizing: border-box; margin: 0; padding: 0; }
  html, body { width: 1200px; height: 844px; overflow: hidden; }
  body {
    background: var(--backdrop);
    font-family: "Open Sans", Arial, sans-serif;
    position: relative;
  }
  .card {
    position: absolute;
    top: 272px;
    width: 520px;
    height: 300px;
    overflow: hidden;
    box-shadow: 0 10px 30px rgba(0,0,0,.45);
  }
  /* Front (photo side) */
  .card-front {
    left: 60px;
    background: linear-gradient(160deg, var(--card-dark-edge), var(--card-dark));
    color: var(--white);
  }
  .headshot {
    position: absolute;
    left: 40px;
    bottom: 0;
    width: 250px;
    height: 245px;
    border-radius: 110px 110px 0 0;
    background: linear-gradient(180deg, var(--photo-top) 0%, var(--photo-mid) 40%, var(--photo-low) 72%, var(--photo-low) 100%);
  }
  .front-brand {
    position: absolute;
    left: 285px;
    top: 26px;
    width: 215px;
    text-align: center;
  }
  .brand-dot {
    display: block;
    width: 56px;
    height: 56px;
    border-radius: 50%;
    background: var(--white);
    margin: 0 auto 10px;
  }
  .brand-name {
    font-family: "Oswald", "Arial Narrow", sans-serif;
    font-weight: 700;
    font-size: 31px;
    line-height: 1;
    letter-spacing: .5px;
    white-space: nowrap;
  }
  .contact {
    position: absolute;
    left: 318px;
    top: 142px;
  }
  .person-name { font-weight: 700; font-size: 16px; line-height: 1.2; }
  .person-role { font-size: 14px; color: var(--muted); margin-bottom: 10px; }
  .contact-list { list-style: none; font-size: 13.5px; }
  .contact-list li { display: flex; align-items: center; gap: 8px; line-height: 1.5; }
  .contact-list svg { width: 12px; height: 12px; fill: var(--white); flex: none; }

  /* Back (appointment side) */
  .card-back { left: 620px; background: var(--paper); }
  .card-back svg.shape { position: absolute; inset: 0; }
  .back-brand {
    position: absolute;
    left: 140px;
    top: 14px;
    width: 200px;
    text-align: center;
    color: var(--ink);
  }
  .back-brand .brand-dot { background: var(--ink); width: 50px; height: 50px; margin-bottom: 8px; }
  .back-brand .brand-name { font-size: 28px; }
  .appointment {
    position: absolute;
    left: 40px;
    top: 128px;
    right: 30px;
    color: var(--ink);
  }
  .appointment-title { font-size: 22px; letter-spacing: 1px; margin-left: 10px; line-height: 1.3; }
  .appointment-line { border-top: 1px solid var(--rule); height: 0; margin: 28px 0 0; }
  .appointment-note { font-size: 10.5px; font-weight: 700; margin-top: 22px; text-align: center; }
</style>
</head>
<body>

<section class="card card-front" aria-label="Card front">
  <div class="headshot" role="img" aria-label="Head-and-shoulders portrait of the managing director in a dark suit and tie"></div>

  <div class="front-brand">
    <span class="brand-dot"></span>
    <div class="brand-name">KESTREL WORKS</div>
  </div>

  <div class="contact">
    <div class="person-name">Daniel Hart</div>
    <div class="person-role">Managing Director</div>
    <ul class="contact-list">
      <li><svg viewBox="0 0 24 24"><path d="M6.6 10.8a15 15 0 0 0 6.6 6.6l2.2-2.2c.3-.3.7-.4 1-.2 1.1.4 2.3.6 3.6.6.6 0 1 .4 1 1V20c0 .6-.4 1-1 1A17 17 0 0 1 3 4c0-.6.4-1 1-1h3.5c.6 0 1 .4 1 1 0 1.3.2 2.5.6 3.6.1.3 0 .7-.2 1z"/></svg>044-555 018 220</li>
      <li><svg viewBox="0 0 24 24"><path d="M2 5h20v14H2zM4 7v.5l8 5 8-5V7z"/></svg>hello@kestrelworks.com</li>
      <li><svg viewBox="0 0 24 24"><path d="M10.6 13.4a1 1 0 0 1 0-1.4l3-3a1 1 0 1 1 1.4 1.4l-3 3a1 1 0 0 1-1.4 0zM8 21a5 5 0 0 1-3.5-8.5l2-2 1.4 1.4-2 2a3 3 0 0 0 4.2 4.2l2-2 1.4 1.4-2 2A5 5 0 0 1 8 21zm9.5-7.5-1.4-1.4 2-2a3 3 0 0 0-4.2-4.2l-2 2-1.4-1.4 2-2a5 5 0 0 1 7 7z"/></svg>www.kestrelworks.com</li>
    </ul>
  </div>
</section>

<section class="card card-back" aria-label="Card back">
  <svg class="shape" width="520" height="300" viewBox="0 0 520 300" aria-hidden="true">
    <rect x="0" y="0" width="520" height="120" fill="var(--card-dark)"/>
    <circle cx="240" cy="95" r="170" fill="var(--paper)"/>
  </svg>

  <div class="back-brand">
    <span class="brand-dot"></span>
    <div class="brand-name">KESTREL WORKS</div>
  </div>

  <div class="appointment">
    <div class="appointment-title">Your Next Appointment :</div>
    <div class="appointment-line"></div>
    <div class="appointment-line"></div>
    <p class="appointment-note">Please give 24 hours notice if you need to reschedule your appointment</p>
  </div>
</section>

</body>
</html>
```